Craft Website Redesign Project

To do...
Design 1 html/css template for home page layout
Design 1 html/css template for products page layout
Design 1 html/css template for gallery page layout
Note: All layouts should have the same look and feel (not 4 different designs). The Home page will have no side menu.

A Photoshop file will do if someone doesn't do html/css however it could effect our decision as i have limited time to work on things like this, i would rather be buried in php code :-)

We need a new website design for our company Meadowlark Papercraft. We are a Rubber Stamp & Scrapbook Manufacture for the Craft industry. Our current products can be viewed at www.meadowlarkpapercraft.us Our most popular items are in the New Products category.
We are looking for a nice clean cut & feel website yet elegant. Easy to use and browse, menu navigation is up for ideas but we like www.tindervalecardworks.com
Company colors are Burgundy, Cream, and White, blues are okay

To give an idea on the kind of work we like visit www.meadowlarkpapercraft.us/adsamples/ this page has 2 links to current Ads we are running.
Updates

I will be posting an update later today with the required layout of our Site Index.

A new file has been attached to this project with the Menu navigation layout.

Target Market(s)

Scrapbookers

Industry/Entity Type

Industry

Requirements
Must have
• Customized look buttons for Facebook, YouTube, Twitter, Pinterest, Blog, & RSS
We don't just want the ordinary colors that these companies provide by default.

```html
<!DOCTYPE html>
<html lang="en">
<head>
<meta charset="utf-8">
<title>Meadowlark Papercraft</title>
<link href="https://fonts.googleapis.com/css2?family=Lobster&family=Lora:ital,wght@0,400;0,700;1,400&family=Open+Sans:wght@400;600&display=swap" rel="stylesheet">
<style>
:root{
  --burgundy:#9c1d45;
  --burgundy-dark:#7d1236;
  --burgundy-light:#b53a62;
  --cream:#f2e6dd;
  --cream-dark:#e6d5c8;
  --page:#dcdadb;
  --ink:#5a2a2a;
  --ink-dark:#2c2326;
  --white:#ffffff;
}
*{margin:0;padding:0;box-sizing:border-box}
html,body{width:1200px;height:1136px;overflow:hidden}
body{position:relative;background:linear-gradient(#e4e2e3,#d3d1d2 900px);font-family:"Lora",serif;color:var(--ink)}
.abs{position:absolute}

.topnav{left:0;top:0;width:1200px;height:54px;background:linear-gradient(var(--burgundy),var(--burgundy-dark));border-bottom:3px dotted #e8c9d3}
.topnav ul{list-style:none;position:absolute;left:138px;top:17px;display:flex}
.topnav li{font-style:italic;font-size:15.5px;color:#f6e3ea;margin-right:26px;white-space:nowrap}
.search{left:936px;top:17px;width:135px;height:21px;border-radius:11px;background:var(--white);box-shadow:inset 0 1px 3px rgba(0,0,0,.3)}
.search svg{position:absolute;right:8px;top:5px}

.brand{left:120px;top:112px;font-family:"Lora",serif;font-style:italic;font-size:39px;color:var(--ink-dark);line-height:1;white-space:nowrap}
.brand-dot{left:122px;top:88px;width:34px;height:34px;border-radius:50%;background:var(--burgundy)}
.brand .name{padding-left:42px}
.tagline{left:282px;top:169px;font-family:"Open Sans",sans-serif;font-weight:600;font-size:17px;color:var(--ink-dark)}

.shoplinks{top:139px;left:849px;display:flex;gap:14px;font-style:italic;font-size:15px;color:#5b3a2c}
.shoplinks span{display:flex;align-items:center;gap:8px}

.slider{left:120px;top:217px;width:960px;height:416px;background:var(--white);box-shadow:0 4px 8px rgba(0,0,0,.25);border-radius:2px}
.slide-art{position:absolute;left:5px;top:4px;width:950px;height:407px;background:linear-gradient(120deg,#c5445a 0%,#c5445a 7%,#ede6da 8%,#ede6da 40%,#c88a6a 45%,#e3a8ac 60%,#c64a5e 100%)}
.caption{left:619px;top:383px;width:410px;height:213px;background:rgba(248,236,232,.82);padding:20px 28px}
.caption h2{font-family:"Lobster",cursive;font-weight:400;font-size:38px;color:var(--burgundy);line-height:1}
.caption p{margin-top:14px;font-style:italic;font-size:16.8px;letter-spacing:-.2px;line-height:21.5px;text-align:justify;color:#4a3b3a}
.btn-dark{left:906px;top:539px;width:101px;height:34px;border-radius:4px;background:linear-gradient(#4a4a4a,#111);color:var(--white);font-family:"Lobster",cursive;font-size:17px;text-align:center;line-height:33px;box-shadow:0 1px 2px rgba(0,0,0,.5)}
.arrow{width:56px;height:56px;top:402px}

.card{top:665px;width:287px;height:257px;background:linear-gradient(var(--cream),#efe1d8);box-shadow:0 4px 6px rgba(0,0,0,.22)}
.ribbon{top:683px;width:318px;height:40px}
.ribbon h3{position:absolute;left:97px;top:5px;font-family:"Lobster",cursive;font-weight:400;font-size:22.5px;color:var(--white);text-shadow:0 1px 1px rgba(0,0,0,.35);white-space:nowrap}
.flower{top:675px;width:56px;height:56px;border-radius:50%;background:radial-gradient(circle,#d9a0b8 0 3px,#2a2a2a 4px,#0c0c0c 100%)}
.card-body{position:absolute;left:23px;top:76px;width:242px;font-size:13.6px;line-height:18.75px;text-align:justify;color:#5b2424}
.card-body .post-date{font-style:italic;font-size:11.5px;margin-bottom:9px}
.more{position:absolute;left:24px;top:212px;font-family:"Lobster",cursive;font-size:18px;color:var(--ink-dark)}
.product-photo{position:absolute;left:23px;top:77px;width:243px;height:130px;background:linear-gradient(135deg,#6b5058,#c8707c 45%,#8a8f60 70%,#3a2f33)}

.lace{left:0;top:973px;width:1200px;height:32px;background:linear-gradient(#555 0,#1c1c1c 40%,#0d0d0d 100%)}
.footer{left:0;top:1005px;width:1200px;height:131px;background:linear-gradient(#b3345a,#9e1f47 60%,#962044)}
.footer h4{position:absolute;left:139px;top:17px;font-family:"Lobster",cursive;font-weight:400;font-size:23px;color:var(--white);text-shadow:0 1px 2px rgba(0,0,0,.35)}
.email{position:absolute;left:141px;top:61px;width:228px;height:29px;background:var(--white);border:1px solid #c9a0ae;font-family:"Open Sans",sans-serif;font-size:13px;color:#222;padding:6px 9px}
.subscribe{position:absolute;left:379px;top:61px;width:87px;height:29px;background:linear-gradient(#3e3e3e,#111);border-radius:3px;color:var(--white);font-family:"Open Sans",sans-serif;font-size:12.5px;text-align:center;line-height:29px}
.payments{position:absolute;left:856px;top:19px;display:flex;gap:5px}
.payments span{width:47px;height:23px;border-radius:2px;background:linear-gradient(#fbfbfb,#dcdcdc);border:1px solid #c7c7c7}
.legal{position:absolute;right:138px;top:61px;text-align:right;font-family:"Open Sans",sans-serif;font-size:11.5px;line-height:17px;color:#f8e1e9}
</style>
</head>
<body>

<nav class="topnav abs">
  <ul>
    <li>Home</li><li>About</li><li>Contact</li><li>Gallery</li><li>Videos</li><li>Blog</li><li>Design Team</li><li>Shows</li><li>Classes</li><li>Products</li>
  </ul>
</nav>
<div class="search abs"><svg width="12" height="12" viewBox="0 0 12 12"><circle cx="5" cy="5" r="3.5" fill="none" stroke="#999" stroke-width="1.5"/><line x1="7.5" y1="7.5" x2="11" y2="11" stroke="#999" stroke-width="1.8"/></svg></div>

<div class="brand-dot abs"></div>
<div class="brand abs"><span class="name">Meadowlark Papercraft</span></div>
<div class="tagline abs">PRINT. TRIM. MAKE.</div>

<div class="shoplinks abs">
  <span><svg width="21" height="15" viewBox="0 0 21 15"><rect x="1" y="1" width="19" height="13" fill="#f0b25c" stroke="#b0621c"/><path d="M1 5h19M1 9h19M6 1v13M11 1v13M16 1v13" stroke="#b0621c"/></svg>Check Order</span>
  <span><svg width="21" height="18" viewBox="0 0 21 18"><path d="M2 6h17l-2 11H4z" fill="#3a8fd6"/><path d="M7 6V1M11 6V0M15 6V2" stroke="#2a6fb0" stroke-width="2"/></svg>Buy Now</span>
</div>

<div class="slider abs">
  <div class="slide-art" role="img" aria-label="Scrapbook paper collage with striped and polka dot papers, a pink button and a small leaf"></div>
</div>
<div class="caption abs">
  <h2>Rubber Art Stamps</h2>
  <p>Sed sed enim dolor, eget fringilla erat. Sed quam velit, rutrum vitae ullamcorper quis, pulvinar sed diam. Maecenas adipiscing auctor placerat.</p>
</div>
<div class="btn-dark abs">Buy Now</div>

<svg class="arrow abs" style="left:91px" viewBox="0 0 56 56"><circle cx="28" cy="28" r="27" fill="#d8c8b0" stroke="#b9a68a" stroke-width="2"/><circle cx="28" cy="28" r="22" fill="#e6dac6"/><path d="M32 19l-9 9 9 9" fill="none" stroke="#8b7862" stroke-width="5" stroke-linecap="round" stroke-linejoin="round"/></svg>
<svg class="arrow abs" style="left:1051px" viewBox="0 0 56 56"><circle cx="28" cy="28" r="27" fill="#d8c8b0" stroke="#b9a68a" stroke-width="2"/><circle cx="28" cy="28" r="22" fill="#e6dac6"/><path d="M24 19l9 9-9 9" fill="none" stroke="#8b7862" stroke-width="5" stroke-linecap="round" stroke-linejoin="round"/></svg>

<section class="card abs" style="left:134px">
  <div class="card-body">December is a great time to visit our Limited Edition section and purchase retiring stamps that will no longer be available for purchase in 2012. Meadowlark Papercraft launches new product releases on the second Wednesday of every month.</div>
  <div class="more">read more</div>
</section>
<section class="card abs" style="left:456px">
  <div class="card-body">
    <div class="post-title">Merry Christmas!</div>
    <div class="post-date">Wednesday, Dec 21</div>
    Hi Everyone, We wish you and your family a very Merry Christmas! I know that for many of us, there are so many things to do and places to go...
  </div>
  <div class="more">read more</div>
</section>
<section class="card abs" style="left:777px">
  <div class="product-photo" role="img" aria-label="Handmade paper roses in pink and sage on a card"></div>
  <div class="more">see more</div>
</section>

<div class="ribbon abs" style="left:120px">
  <svg width="318" height="40" viewBox="0 0 318 40"><path d="M0 0h14v40H0l6-20z" fill="var(--burgundy-dark)"/><path d="M318 0h-14v40h14l-6-20z" fill="var(--burgundy-dark)"/><rect x="12" y="0" width="294" height="40" fill="var(--burgundy)"/><rect x="12" y="0" width="294" height="3" fill="var(--burgundy-light)"/></svg>
  <h3>News &amp; Product Info</h3>
</div>
<div class="ribbon abs" style="left:442px">
  <svg width="318" height="40" viewBox="0 0 318 40"><path d="M0 0h14v40H0l6-20z" fill="var(--burgundy-dark)"/><path d="M318 0h-14v40h14l-6-20z" fill="var(--burgundy-dark)"/><rect x="12" y="0" width="294" height="40" fill="var(--burgundy)"/><rect x="12" y="0" width="294" height="3" fill="var(--burgundy-light)"/></svg>
  <h3 style="left:95px">Recent Blogs</h3>
</div>
<div class="ribbon abs" style="left:763px">
  <svg width="318" height="40" viewBox="0 0 318 40"><path d="M0 0h14v40H0l6-20z" fill="var(--burgundy-dark)"/><path d="M318 0h-14v40h14l-6-20z" fill="var(--burgundy-dark)"/><rect x="12" y="0" width="294" height="40" fill="var(--burgundy)"/><rect x="12" y="0" width="294" height="3" fill="var(--burgundy-light)"/></svg>
  <h3 style="left:97px">New Products</h3>
</div>
<div class="flower abs" style="left:151px" role="img" aria-label="Black fabric flower with a pink pearl centre"></div>
<div class="flower abs" style="left:473px" role="img" aria-label="Black fabric flower with a pink pearl centre"></div>
<div class="flower abs" style="left:794px" role="img" aria-label="Black fabric flower with a pink pearl centre"></div>

<div class="lace abs" role="img" aria-label="Black lace trim"></div>

<footer class="footer abs">
  <h4>Get Update to Our Newsletter</h4>
  <div class="email">E-mail</div>
  <div class="subscribe">SUBSCRIBE</div>
  <div class="payments"><span></span><span></span><span></span><span></span></div>
  <div class="legal">Copyright © 2006 - 2011 Meadowlark Papercraft All Rights Reserved<br>Site By: Brightquill Web Studio</div>
</footer>

</body>
</html>
```